Home Services- Spring Clean Options

Brightwell Crew provides a variety of Home Services- focused on cleaning & improving the exterior of the home:

 Power Washing- driveways, sidewalks, patios, decks, fence
 Fence Staining- make fence look new with variety of staining colors
 Gutter cleaning- important to make sure have proper Water Drainage
 Gutter Guard Installation- prevent damage to roof and house by keeping debris out of gutters and water flowing.
 Window Washing- our exterior washing team and reach the highest windows
 Landscape& Patio Lights- highlight areas for beauty and safety
Updates

We are are almost finished. Just please make sure you pay attention to the wording and grammer in Red thx

Target Market(s)

Middle to Upper level Home Owners (especially women)

Industry/Entity Type

Cleaning Services

Font styles to use
Serif
Sans Serif

Requirements
Must have
• Not be Cluttered- Clean friendly, professional look. Focus on the Professional

Info@GoBrightwellCrew.com
972-648-0000
Nice to have
• Pictures of services- these are just examples
Should not have
• Bigger and bolder Services & Specials. Want to Show all the Services we offer but do Not use too much detail- don't want it to look "cluttered"

```html
<!DOCTYPE html>
<html lang="en">
<head>
<meta charset="utf-8">
<title>Brightwell Crew – Home Services Flyer</title>
<link href="https://fonts.googleapis.com/css2?family=Poppins:wght@300;400;600;700&display=swap" rel="stylesheet">
<style>
  :root{
    --navy:#22357f;
    --navy-deep:#13275a;
    --sky:#27a3e0;
    --ink:#2a2a2a;
    --paper:#ffffff;
    --backdrop:#b3b3b3;
  }
  *{margin:0;padding:0;box-sizing:border-box}
  html,body{width:1200px;height:1200px;overflow:hidden}
  body{background:var(--backdrop);font-family:'Poppins',sans-serif;position:relative}
  .flyer{position:absolute;left:190px;top:20px;width:820px;height:1160px;background:var(--paper);overflow:hidden}
  .flyer-art{position:absolute;inset:0}
  .headline{position:absolute;right:55px;top:700px;text-align:right;color:var(--ink);line-height:1}
  .headline .brand{display:block;color:var(--navy);font-weight:700;font-size:34px;letter-spacing:.3px}
  .headline .lead{display:block;font-weight:300;font-size:32px;margin-top:8px;letter-spacing:.5px}
  .headline .title{display:block;font-weight:400;font-size:50px;margin-top:6px}
  .headline-rule{position:absolute;left:782px;top:702px;width:1.5px;height:125px;background:var(--navy)}
  .tagline{position:absolute;right:56px;top:826px;color:var(--navy);font-size:20.5px;font-weight:400}
  .services-heading{position:absolute;left:0;width:820px;top:863px;text-align:center;font-weight:700;font-size:18px;color:var(--ink);letter-spacing:.5px;padding-left:0}
  .services-heading span{position:relative;left:0}
  .service-list{position:absolute;list-style:none;font-size:14px;line-height:17px;color:var(--ink)}
  .service-list.left{left:49px;top:925px;width:320px}
  .service-list.right{left:423px;top:925px;width:345px}
  .service-list li{position:relative;padding-left:26px;margin-bottom:11px}
  .service-list.right li{padding-left:20px}
  .service-list li .name{color:var(--sky);font-weight:700;letter-spacing:.3px}
  .service-list li svg{position:absolute;left:0;top:2px;width:14px;height:14px}
  .col-divider{position:absolute;left:394px;top:911px;width:4px;height:188px;background:linear-gradient(to right,rgba(0,0,0,.08),rgba(0,0,0,0));border-radius:2px}
  .contact{position:absolute;left:481px;color:var(--paper);font-weight:300}
  .contact.phone{top:1082px;font-size:19px}
  .contact.phone b{font-weight:700}
  .contact.web{top:1120px;font-size:13.5px;letter-spacing:.2px}
  .contact.web b{font-weight:600}
</style>
</head>
<body>
<main class="flyer">
  <svg class="flyer-art" width="820" height="1160" viewBox="0 0 820 1160">
    <defs>
      <linearGradient id="garden-tones" x1="0" y1="0" x2="1" y2="1">
        <stop offset="0" stop-color="#3f6b35"/><stop offset=".5" stop-color="#6f8a55"/><stop offset="1" stop-color="#b9a98d"/>
      </linearGradient>
      <linearGradient id="washing-tones" x1="0" y1="0" x2="1" y2="1">
        <stop offset="0" stop-color="#6e8c4a"/><stop offset=".6" stop-color="#9fae86"/><stop offset="1" stop-color="#d9d6cc"/>
      </linearGradient>
      <radialGradient id="uplight-tones" cx=".5" cy=".6" r=".6">
        <stop offset="0" stop-color="#a07a4a"/><stop offset=".6" stop-color="#3c3327"/><stop offset="1" stop-color="#1b2230"/>
      </radialGradient>
      <radialGradient id="patio-tones" cx=".5" cy=".4" r=".6">
        <stop offset="0" stop-color="#c9a86a"/><stop offset=".6" stop-color="#4b5a3a"/><stop offset="1" stop-color="#2a2f2a"/>
      </radialGradient>
      <linearGradient id="night-panel" x1="0" y1="0" x2="1" y2="1">
        <stop offset="0" stop-color="#1f3a78"/><stop offset="1" stop-color="#0f2150"/>
      </linearGradient>
    </defs>

    <!-- left navy panel and top-right corner -->
    <rect x="0" y="0" width="260" height="820" fill="url(#night-panel)" role="img" aria-label="Dark blue toned evening garden backdrop"/>
    <path d="M640 0 H820 V112 Q780 25 640 0 Z" fill="var(--navy)"/>

    <!-- main photo area -->
    <path d="M48 0 Q40 330 150 420" fill="none" stroke="var(--sky)" stroke-width="12"/>
    <path d="M75 0 L663 0 Q780 25 820 112 L820 522 Q690 585 520 580 L200 560 Q80 420 75 0 Z" fill="url(#garden-tones)" stroke="var(--paper)" stroke-width="8" role="img" aria-label="Family enjoying a backyard cookout by an outdoor stone kitchen and grill"/>

    <!-- white lower field -->
    <path d="M0 800 C40 700 110 640 240 610 L540 600 Q700 595 820 540 V1160 H0 Z" fill="var(--paper)"/>
    <path d="M0 795 C40 700 110 645 240 612" fill="none" stroke="var(--sky)" stroke-width="7"/>
    <path d="M540 598 Q710 590 820 536" fill="none" stroke="var(--sky)" stroke-width="12"/>

    <!-- service photo circles -->
    <circle cx="244" cy="694" r="106" fill="var(--paper)"/>
    <circle cx="244" cy="694" r="102" fill="url(#patio-tones)" stroke="var(--sky)" stroke-width="3" role="img" aria-label="Patio at night under strings of bistro lights"/>
    <circle cx="423" cy="563" r="114" fill="var(--paper)"/>
    <circle cx="423" cy="563" r="106" fill="url(#uplight-tones)" stroke="var(--sky)" stroke-width="3" role="img" aria-label="Trees lit by landscape uplights beside a pool"/>
    <circle cx="195" cy="460" r="162" fill="var(--paper)"/>
    <circle cx="195" cy="460" r="154" fill="url(#washing-tones)" stroke="var(--sky)" stroke-width="4" role="img" aria-label="Power washing a concrete sidewalk"/>

    <!-- services divider -->
    <path d="M130 853 V875 H344 M473 875 H782 V853" fill="none" stroke="var(--navy)" stroke-width="1.2"/>

    <!-- bottom bands -->
    <path d="M0 1127 Q250 1128 448 1146 L448 1160 H0 Z" fill="var(--sky)"/>
    <path d="M380 1144 L448 1140 L448 1150 Z" fill="var(--navy)"/>
    <path d="M472 1061 H820 V1160 H448 V1150 Q452 1140 448 1118 Q440 1112 448 1100 Q452 1090 448 1082 Q448 1061 472 1061 Z" fill="var(--sky)"/>

    <!-- contact icons -->
    <circle cx="451" cy="1096" r="11" fill="var(--paper)"/>
    <path d="M446 1090 q-2 2 0 6 q3 5 8 7 q3 1 4 -1 l-1 -2 l-3 -1 l-1 1 q-3 -2 -4 -4 l1 -1 l-1 -3 z" fill="var(--navy-deep)"/>
    <circle cx="451" cy="1129" r="11" fill="var(--paper)"/>
    <circle cx="451" cy="1129" r="6" fill="none" stroke="var(--navy-deep)" stroke-width="1.3"/>
    <path d="M445 1129 H457 M451 1123 Q447 1129 451 1135 Q455 1129 451 1123" fill="none" stroke="var(--navy-deep)" stroke-width="1"/>
  </svg>

  <h1 class="headline">
    <span class="brand">BRIGHTWELL CREW</span>
    <span class="lead">PROVIDES A VARIETY OF</span>
    <span class="title">HOME SERVICES</span>
  </h1>
  <div class="headline-rule"></div>
  <p class="tagline">Focused on cleaning &amp; improving the exterior of the home:</p>
  <h2 class="services-heading"><span>SERVICES:</span></h2>

  <ul class="service-list left">
    <li><svg viewBox="0 0 14 14"><circle cx="7" cy="7" r="7" fill="var(--sky)"/><path d="M4 7.2 L6.2 9.2 L10 5" fill="none" stroke="#fff" stroke-width="1.6"/></svg><span class="name">POWER WASHING-</span> driveways, sidewalks, patios, decks, fence</li>
    <li><svg viewBox="0 0 14 14"><circle cx="7" cy="7" r="7" fill="var(--sky)"/><path d="M4 7.2 L6.2 9.2 L10 5" fill="none" stroke="#fff" stroke-width="1.6"/></svg><span class="name">FENCE STAINING-</span> make fence look new with variety of staining colors</li>
    <li><svg viewBox="0 0 14 14"><circle cx="7" cy="7" r="7" fill="var(--sky)"/><path d="M4 7.2 L6.2 9.2 L10 5" fill="none" stroke="#fff" stroke-width="1.6"/></svg><span class="name">GUTTER CLEANING-</span> important to make sure have proper Water Drainage</li>
    <li><svg viewBox="0 0 14 14"><circle cx="7" cy="7" r="7" fill="var(--sky)"/><path d="M4 7.2 L6.2 9.2 L10 5" fill="none" stroke="#fff" stroke-width="1.6"/></svg><span class="name">WINDOW WASHING-</span> our exterior washing team and reach the highest windows</li>
  </ul>
  <div class="col-divider"></div>
  <ul class="service-list right">
    <li><svg viewBox="0 0 14 14"><circle cx="7" cy="7" r="7" fill="var(--sky)"/><path d="M4 7.2 L6.2 9.2 L10 5" fill="none" stroke="#fff" stroke-width="1.6"/></svg><span class="name">GUTTER GUARD INSTALLATION-</span> prevent damage to roof and house by keeping debris out of gutters and water flowing</li>
    <li><svg viewBox="0 0 14 14"><circle cx="7" cy="7" r="7" fill="var(--sky)"/><path d="M4 7.2 L6.2 9.2 L10 5" fill="none" stroke="#fff" stroke-width="1.6"/></svg><span class="name">LANDSCAPE&amp; PATIO LIGHTS-</span> highlight areas for beauty and safety</li>
  </ul>

  <p class="contact phone">CALL NOW: <b>972-648-0000</b></p>
  <p class="contact web">WWW.<b>BRIGHTWELLCREWHOME</b>.COM</p>
</main>
</body>
</html>
```